Grivo like IOS/Android app for Okinawa Island - TavuScout

TavuScout is the name of the app
The closest thing that I can relate this app to is a region specific Grivo app. The app is for the island of Okinawa and is geared towards English speaking travelers. The style of app that I prefer is a look and feel similar to that of the new Lodgemere app, color should also be similar if not the same as the lodgemere app.

The app needs to have the following screens

LOGIN SCREEN
1. App login page with a login for chatterly button or create an account option. Personally I would like an image in the background with a real beachy feel, but don't do this if it messes with your design.

2. Depending on the choice of login there will need to be a second login screen to create the account. Lodgemere does this nicely.

PRIMARY HOME
primary page similar to the primary layout when you get into the lodgemere app.
This page is kind of like the home page of the app and should include the following items:
search field
upcoming events
popular things to do
featured restaurants
Featured Places to stay
area guides
Moving here
(this will allow the person to select, housing agencies, auto dealers, schools etc) These are essentially just quick searches.
Each selection should be listed so that the user can swipe to the left or right in order to view more listings under the categories listed above. It will not be the full list but rather a sample.

SIDEBAR POPOUT MENU
Popout sidebar that contains the following selections
Places to Eat
Things to do
Attractions
Beaches
Shop
Farmers Markets
Places to Stay
Schools & DayCare
Housing
Auto
Events
Account settings
Add a business

LIST VIEW
4. List view page for whatever category the user selected. This will show all the listings for the specific category: The top should also have the featured listings for that category

INDIVIDUAL LISTING
5. Listing page
This will include photos, description, hours, map(this can be a button to view the map or the map), Reviews with a leave a review option

AREA GUIDES
6. Area Guides. This is where the user will be able to select a specific area and learn about it. It should include an area where there can be a description, photos with a hero photo image, a map, popular local attractions or things to do, best restaurants in the area, places to stay etc.

PROFILE PAGE
7. Profile page for the user where they can make any updates they need to

Every page but the listing page should include the search bar. When the user clicks in it they should be able to see a drop down of quick select searches or run a regular search.

Logo
I have attached a logo that was made that needs a redesign. The map marker contains the logo for Okinawa within it so it does need to be similar.

If you have any questions or need clarification please send me a message. I will respond promptly.
Thank you,

```html
<!DOCTYPE html>
<html lang="en">
<head>
<meta charset="utf-8">
<title>TavuScout app screens</title>
<link href="https://fonts.googleapis.com/css2?family=Lato:wght@300;400;700&display=swap" rel="stylesheet">
<style>
:root{
  --stage:#262626;
  --coral:#e85d6a;
  --coral-deep:#d84a59;
  --coral-line:#f3b3b9;
  --red-btn:#d9493e;
  --blue-btn:#3d5ee0;
  --white:#ffffff;
  --ink:#333333;
  --muted:#8a8a8a;
  --soft:#ececec;
  --gold:#f5b400;
}
*{box-sizing:border-box;margin:0;padding:0}
html,body{width:1200px;height:1200px;overflow:hidden;background:var(--stage);font-family:'Lato',sans-serif}
.screen{position:absolute;width:220px;height:389px;overflow:hidden;background:var(--coral);color:var(--white)}
.abs{position:absolute}
.status{position:absolute;top:0;left:0;right:0;height:13px;font-size:6.5px;font-weight:700;display:flex;justify-content:space-between;align-items:center;padding:0 5px;color:var(--white)}
.status.dark{color:var(--ink)}
.photo-sunset{position:absolute;inset:0;background:linear-gradient(180deg,#4a2a4a 0%,#8a2f3a 22%,#e0542a 40%,#f0a030 47%,#b8321e 55%,#3a0d0d 75%,#1a0505 100%)}
.center{left:0;right:0;text-align:center}
.h-app{font-size:21px;font-weight:700}
.tagline{font-size:14.5px;font-weight:300;line-height:19px}
.btn{position:absolute;left:14px;width:192px;height:25px;font-size:9.5px;display:flex;align-items:center;justify-content:center;gap:8px;color:var(--white)}
.btn .sq{width:12px;height:12px;background:var(--white);opacity:.9}
.field-label{position:absolute;left:14px;right:14px;text-align:center;font-size:8.5px}
.field-line{position:absolute;left:14px;right:14px;height:1px;background:var(--white);opacity:.85}
.back{position:absolute;left:12px;top:30px}
.q-title{position:absolute;left:0;right:0;text-align:center;font-size:16px;font-weight:700;top:88px}
.q-note{position:absolute;left:18px;right:18px;text-align:center;font-size:8.5px;line-height:10.5px;top:116px;opacity:.95}
.next{position:absolute;left:178px;top:344px;width:31px;height:31px;border-radius:50%;background:#f08792;display:flex;align-items:center;justify-content:center}
.appbar{position:absolute;top:0;left:0;right:0;height:42px;background:var(--coral)}
.appbar .title{position:absolute;top:20px;left:0;right:0;text-align:center;font-size:10.5px}
.appbar .ic{position:absolute;top:22px}
.list-bg{position:absolute;top:42px;left:0;right:0;bottom:0;background:var(--soft)}
.row{position:absolute;left:6px;width:208px;height:25px;background:var(--white);color:var(--ink);font-size:10.5px;display:flex;align-items:center;padding-left:8px;gap:13px}
.row .chev{position:absolute;right:9px;top:8px}
.pop{position:absolute;left:7px;font-size:9px;color:var(--ink)}
.pop b{color:var(--coral);font-weight:400}
.food{position:absolute;left:0;right:0;height:75px}
.food .bar{position:absolute;left:0;right:0;bottom:0;height:22px;background:rgba(40,40,40,.65);color:var(--white);padding:2px 8px}
.food .name{font-size:9.5px;font-weight:700}
.food .loc{font-size:5.5px;opacity:.85}
.food .open{position:absolute;right:26px;top:2px;font-size:8.5px;color:#f08a4a;text-align:right}
.food .hrs{position:absolute;right:14px;top:12px;font-size:6px;color:var(--white)}
.menu{position:absolute;left:20px;top:86px}
.menu li{list-style:none;height:20px;display:flex;align-items:center;gap:12px;font-size:9.5px;font-weight:700}
.menu .mi{width:9px;height:9px;border:1.5px solid var(--white);border-radius:2px}
.listing{position:absolute;left:0;right:0;height:57px;background:var(--white);border-bottom:1px solid #e5e5e5;color:var(--ink)}
.listing .thumb{position:absolute;left:6px;top:5px;width:46px;height:46px}
.listing .n{position:absolute;left:63px;top:6px;font-size:8px}
.listing .d{position:absolute;left:63px;top:16px;font-size:5px;color:#aaa;line-height:6.5px;width:130px}
.listing .stars{position:absolute;left:63px;top:33px;font-size:7px;color:var(--gold);letter-spacing:2px}
.listing .stars i{color:#ddd;font-style:normal}
.listing .price{position:absolute;left:63px;top:44px;font-size:7px}
.listing .km{position:absolute;right:6px;top:44px;font-size:6px;color:var(--muted)}
.ad{position:absolute;right:0;top:0;width:0;height:0;border-top:16px solid #f4c56a;border-left:16px solid transparent}
</style>
</head>
<body>

<!-- ROW 1 -->
<section class="screen" style="left:150px;top:6px">
  <div class="photo-sunset" role="img" aria-label="Photo of a sunset over the sea with the sun low on the horizon"></div>
  <div class="status"><span>●●○○○ NordaTel</span><span>14:39</span><span>▭</span></div>
  <div class="abs" style="left:54px;top:190px;display:flex;align-items:center;gap:6px">
    <span style="width:16px;height:16px;border-radius:50%;background:var(--white)"></span>
    <span style="font-size:19px;font-weight:400">TavuScout</span>
  </div>
</section>

<section class="screen" style="left:374px;top:6px">
  <div class="photo-sunset" role="img" aria-label="Photo of a sunset over the sea"></div>
  <div class="status"><span>●●○○○ NordaTel</span><span>14:39</span><span>▭</span></div>
  <div class="abs center h-app" style="top:58px">TavuScout</div>
  <div class="abs center tagline" style="top:80px">TavuScout is your local guide<br>to finding just the place to eat,<br>shop, drink, relax, and play</div>
  <div class="btn" style="top:298px;background:var(--blue-btn)"><span class="sq"></span>START WITH CHATTERLY</div>
  <div class="btn" style="top:328px;background:var(--red-btn)"><span class="sq"></span>START WITH GLINTLY</div>
  <div class="abs center" style="top:372px;font-size:8px;color:#f08a5a">Already have an account? <span style="color:var(--white)">Login</span></div>
</section>

<section class="screen" style="left:600px;top:6px">
  <div class="photo-sunset" role="img" aria-label="Photo of a sunset over the sea"></div>
  <div class="status"><span>●●○○○ NordaTel</span><span>14:39</span><span>▭</span></div>
  <div class="abs center h-app" style="top:58px">TavuScout</div>
  <div class="abs center tagline" style="top:80px">TavuScout is your local guide<br>to finding just the place to eat,<br>shop, drink, relax, and play</div>
  <div class="field-label" style="top:184px">Email</div><div class="field-line" style="top:198px"></div>
  <div class="field-label" style="top:212px">Password</div><div class="field-line" style="top:226px"></div>
  <div class="btn" style="top:244px;height:26px;background:var(--red-btn);font-size:10px">LOGIN</div>
  <div class="abs center" style="top:286px;font-size:8px">Forgot Password?</div>
  <div class="abs center" style="top:325px;font-size:8px">Don't have an account? <b>Signup</b></div>
</section>

<section class="screen" style="left:826px;top:6px">
  <div class="status"><span>●●○○○ NordaTel</span><span>14:39</span><span>▭</span></div>
  <svg class="back" width="14" height="10" viewBox="0 0 14 10"><path d="M13 5H2M6 1L2 5l4 4" stroke="#fff" stroke-width="1.3" fill="none"/></svg>
  <div class="q-title" style="top:88px">What's your name?</div>
  <div class="field-label" style="top:154px">First name</div><div class="field-line" style="top:168px"></div>
  <div class="field-label" style="top:195px">Last name</div><div class="field-line" style="top:208px"></div>
  <div class="next"><svg width="10" height="14" viewBox="0 0 10 14"><path d="M2 1l6 6-6 6" stroke="#fff" stroke-width="1.4" fill="none"/></svg></div>
</section>

<!-- ROW 2 -->
<section class="screen" style="left:150px;top:406px">
  <div class="status"><span>●●○○○ NordaTel</span><span>14:39</span><span>▭</span></div>
  <svg class="back" width="14" height="10" viewBox="0 0 14 10"><path d="M13 5H2M6 1L2 5l4 4" stroke="#fff" stroke-width="1.3" fill="none"/></svg>
  <div class="q-title">Your email?</div>
  <div class="field-label" style="top:153px">Email Address</div><div class="field-line" style="top:167px"></div>
  <div class="next"><svg width="10" height="14" viewBox="0 0 10 14"><path d="M2 1l6 6-6 6" stroke="#fff" stroke-width="1.4" fill="none"/></svg></div>
</section>

<section class="screen" style="left:380px;top:406px">
  <div class="status"><span>●●○○○ NordaTel</span><span>14:39</span><span>▭</span></div>
  <svg class="back" width="14" height="10" viewBox="0 0 14 10"><path d="M13 5H2M6 1L2 5l4 4" stroke="#fff" stroke-width="1.3" fill="none"/></svg>
  <div class="q-title">Create a password ...</div>
  <div class="q-note">Password must be at least 6 charectors and include a combination of uppercase and lowercase letters &amp; numbers</div>
  <div class="field-label" style="top:174px">Password</div>
  <svg class="abs" style="left:189px;top:176px" width="12" height="7" viewBox="0 0 12 7"><ellipse cx="6" cy="3.5" rx="5.5" ry="3.2" fill="#fff"/><circle cx="6" cy="3.5" r="1.5" fill="var(--coral)"/></svg>
  <div class="field-line" style="top:188px"></div>
  <div class="next"><svg width="10" height="14" viewBox="0 0 10 14"><path d="M2 1l6 6-6 6" stroke="#fff" stroke-width="1.4" fill="none"/></svg></div>
</section>

<section class="screen" style="left:606px;top:406px">
  <div class="status"><span>●●○○○ NordaTel</span><span>14:39</span><span>▭</span></div>
  <svg class="back" width="14" height="10" viewBox="0 0 14 10"><path d="M13 5H2M6 1L2 5l4 4" stroke="#fff" stroke-width="1.3" fill="none"/></svg>
  <div class="q-title">When is your Birthday ?</div>
  <div class="q-note">You must be at least 18 year old to use TavuScout.<br>And we will not share anything with anyone.</div>
  <div class="field-label" style="top:174px">Password</div>
  <svg class="abs" style="left:189px;top:176px" width="12" height="7" viewBox="0 0 12 7"><ellipse cx="6" cy="3.5" rx="5.5" ry="3.2" fill="#fff"/><circle cx="6" cy="3.5" r="1.5" fill="var(--coral)"/></svg>
  <div class="field-line" style="top:188px"></div>
  <div class="next"><svg width="10" height="14" viewBox="0 0 10 14"><path d="M2 1l6 6-6 6" stroke="#fff" stroke-width="1.4" fill="none"/></svg></div>
</section>

<section class="screen" style="left:830px;top:406px;background:var(--white)">
  <div class="abs" style="left:50px;top:70px;width:120px;height:120px;border-radius:50%;border:3px solid #e6e6e6;background:radial-gradient(circle,#f8e060 0 45%,#ffffff 46%)" role="img" aria-label="Illustration of a hotel building with clouds and two staff figures"></div>
  <div class="abs center" style="top:200px;font-size:13px;color:#555">Near By</div>
  <div class="abs center" style="top:224px;font-size:10px;color:#666;line-height:13px">Search for nearby restaurants, shops,<br>and services</div>
  <div class="abs center" style="top:325px;display:flex;justify-content:center;gap:5px">
    <span style="width:6px;height:6px;border-radius:50%;background:var(--coral)"></span>
    <span style="width:6px;height:6px;border-radius:50%;background:#ddd"></span>
    <span style="width:6px;height:6px;border-radius:50%;background:#ddd"></span>
  </div>
</section>

<!-- ROW 3 : Home -->
<section class="screen" style="left:150px;top:798px;height:394px">
  <div class="list-bg"></div>
  <div class="appbar">
    <div class="status"><span>●●○○○ NordaTel</span><span>14:39</span><span>▭</span></div>
    <svg class="ic" style="left:10px" width="13" height="10" viewBox="0 0 13 10"><path d="M0 1h13M0 5h13M0 9h13" stroke="#fff" stroke-width="1.2"/></svg>
    <div class="title">TavuScout</div>
    <svg class="ic" style="right:9px" width="10" height="10" viewBox="0 0 10 10"><circle cx="4" cy="4" r="3" stroke="#fff" fill="none" stroke-width="1.2"/><path d="M6.3 6.3L9.5 9.5" stroke="#fff" stroke-width="1.2"/></svg>
  </div>
  <div class="row" style="top:47px">▢ Upcoming events<svg class="chev" width="6" height="9" viewBox="0 0 6 9"><path d="M1 1l3.5 3.5L1 8" stroke="#333" fill="none" stroke-width="1.2"/></svg></div>
  <div class="row" style="top:74px">⚘ Popular things to do<svg class="chev" width="6" height="9" viewBox="0 0 6 9"><path d="M1 1l3.5 3.5L1 8" stroke="#333" fill="none" stroke-width="1.2"/></svg></div>
  <div class="row" style="top:101px">ψ Featured restaurants<svg class="chev" width="6" height="9" viewBox="0 0 6 9"><path d="M1 1l3.5 3.5L1 8" stroke="#333" fill="none" stroke-width="1.2"/></svg></div>
  <div class="row" style="top:128px">▦ Featured Places to stay<svg class="chev" width="6" height="9" viewBox="0 0 6 9"><path d="M1 1l3.5 3.5L1 8" stroke="#333" fill="none" stroke-width="1.2"/></svg></div>
  <div class="row" style="top:155px">┳ Area guides<svg class="chev" width="6" height="9" viewBox="0 0 6 9"><path d="M1 1l3.5 3.5L1 8" stroke="#333" fill="none" stroke-width="1.2"/></svg></div>
  <div class="row" style="top:182px">✥ Moving here<svg class="chev" width="6" height="9" viewBox="0 0 6 9"><path d="M1 1l3.5 3.5L1 8" stroke="#333" fill="none" stroke-width="1.2"/></svg></div>
  <div class="pop" style="top:216px">Popular <b>restaurant</b> near by location</div>
  <div class="food" style="top:232px;background:linear-gradient(160deg,#e8e2d6,#c9b79a 50%,#8b8272)" role="img" aria-label="Photo of a plated salad dish">
    <div class="bar"><div class="name">Kaiyo Kitchen</div><div class="loc">⌖ Kokusai Street, Naha</div><div class="open">Open</div><div class="hrs">11 AM - 9 PM</div></div>
  </div>
  <div class="food" style="top:307px;background:linear-gradient(160deg,#d8a060,#b0502c 50%,#6a3a22)" role="img" aria-label="Photo of a pepperoni pizza">
    <div class="bar"><div class="name">Hibiscus Cafe &amp; Restaurant</div><div class="loc">⌖ Kokusai Street, Naha</div><div class="open">Open</div><div class="hrs">10AM - 11 PM</div></div>
  </div>
</section>

<!-- ROW 3 : Home with search -->
<section class="screen" style="left:381px;top:798px;height:394px">
  <div class="list-bg"></div>
  <div class="appbar">
    <div class="status"><span>●●○○○ NordaTel</span><span>14:39</span><span>▭</span></div>
    <svg class="ic" style="left:10px" width="13" height="10" viewBox="0 0 13 10"><path d="M0 1h13M0 5h13M0 9h13" stroke="#fff" stroke-width="1.2"/></svg>
    <div class="title">TavuScout</div>
    <svg class="ic" style="right:9px" width="8" height="11" viewBox="0 0 8 11"><path d="M4 11V1M1 4l3-3 3 3" stroke="#fff" fill="none" stroke-width="1.2"/></svg>
  </div>
  <div class="abs" style="top:42px;left:0;right:0;height:26px;background:var(--coral-deep);font-size:8.5px;padding:8px 10px;display:flex;justify-content:space-between"><span>⌕&nbsp; Search here</span><span>Done</span></div>
  <div class="row" style="top:77px">▢ Upcoming events<svg class="chev" width="6" height="9" viewBox="0 0 6 9"><path d="M1 1l3.5 3.5L1 8" stroke="#333" fill="none" stroke-width="1.2"/></svg></div>
  <div class="row" style="top:104px">⚘ Popular things to do<svg class="chev" width="6" height="9" viewBox="0 0 6 9"><path d="M1 1l3.5 3.5L1 8" stroke="#333" fill="none" stroke-width="1.2"/></svg></div>
  <div class="row" style="top:131px">ψ Featured restaurants<svg class="chev" width="6" height="9" viewBox="0 0 6 9"><path d="M1 1l3.5 3.5L1 8" stroke="#333" fill="none" stroke-width="1.2"/></svg></div>
  <div class="row" style="top:158px">▦ Featured Places to stay<svg class="chev" width="6" height="9" viewBox="0 0 6 9"><path d="M1 1l3.5 3.5L1 8" stroke="#333" fill="none" stroke-width="1.2"/></svg></div>
  <div class="row" style="top:185px">┳ Area guides<svg class="chev" width="6" height="9" viewBox="0 0 6 9"><path d="M1 1l3.5 3.5L1 8" stroke="#333" fill="none" stroke-width="1.2"/></svg></div>
  <div class="row" style="top:212px">✥ Moving here<svg class="chev" width="6" height="9" viewBox="0 0 6 9"><path d="M1 1l3.5 3.5L1 8" stroke="#333" fill="none" stroke-width="1.2"/></svg></div>
  <div class="pop" style="top:246px">Popular <b>restaurant</b> near by location</div>
  <div class="food" style="top:262px;background:linear-gradient(160deg,#e8e2d6,#c9b79a 50%,#8b8272)" role="img" aria-label="Photo of a plated salad dish">
    <div class="bar"><div class="name">Kaiyo Kitchen</div><div class="loc">⌖ Kokusai Street, Naha</div><div class="open">Open</div><div class="hrs">11 AM - 9 PM</div></div>
  </div>
  <div class="food" style="top:337px;background:linear-gradient(160deg,#d8a060,#b0502c 50%,#6a3a22)" role="img" aria-label="Photo of a pepperoni pizza">
    <div class="bar"><div class="name">Hibiscus Cafe &amp; Restaurant</div></div>
  </div>
</section>

<!-- ROW 3 : Sidebar -->
<section class="screen" style="left:610px;top:798px;height:394px;background:var(--coral-deep)">
  <div class="status"><span>●●○○○ NordaTel</span><span>14:39</span><span>▭</span></div>
  <div class="abs" style="left:45px;top:34px;font-size:21px;font-weight:400">TavuScout</div>
  <ul class="menu">
    <li><span class="mi"></span>PLACES TO EAT</li>
    <li><span class="mi"></span>THINGS TO DO</li>
    <li><span class="mi"></span>ATTRACTIONS</li>
    <li><span class="mi"></span>BEACHES</li>
    <li><span class="mi"></span>SHOP</li>
    <li><span class="mi"></span>FARMERS MARKETS</li>
    <li><span class="mi"></span>PLACES TO STAY</li>
    <li><span class="mi"></span>SCHOOLS &amp; DAYCARE</li>
    <li><span class="mi"></span>HOUSING</li>
    <li><span class="mi"></span>AUTO</li>
    <li><span class="mi"></span>EVENTS</li>
    <li><span class="mi"></span>ACCOUNT SETTINGS</li>
    <li><span class="mi"></span>ADD A BUSINESS</li>
  </ul>
  <div class="abs" style="left:180px;top:82px;width:42px;height:232px;background:var(--soft);overflow:hidden">
    <div style="height:22px;background:var(--coral)"></div>
    <div style="margin:4px 3px;height:14px;background:#fff"></div>
    <div style="margin:4px 3px;height:14px;background:#fff"></div>
    <div style="margin:4px 3px;height:14px;background:#fff"></div>
    <div style="margin:4px 3px;height:14px;background:#fff"></div>
    <div style="margin:4px 3px;height:14px;background:#fff"></div>
    <div style="margin:4px 3px;height:14px;background:#fff"></div>
    <div style="height:50px;margin-top:8px;background:linear-gradient(160deg,#e8e2d6,#8b8272)" role="img" aria-label="Photo of a salad dish"></div>
    <div style="height:50px;background:linear-gradient(160deg,#d8a060,#6a3a22)" role="img" aria-label="Photo of a pizza"></div>
  </div>
</section>

<!-- ROW 3 : Restaurant list -->
<section class="screen" style="left:836px;top:798px;height:394px;width:222px;background:var(--white)">
  <div class="appbar">
    <div class="status"><span>●●○○○ NordaTel</span><span>14:39</span><span>▭</span></div>
    <svg class="ic" style="left:10px" width="13" height="10" viewBox="0 0 13 10"><path d="M0 1h13M0 5h13M0 9h13" stroke="#fff" stroke-width="1.2"/></svg>
    <div class="title">Restaurant</div>
    <svg class="ic" style="right:9px" width="10" height="10" viewBox="0 0 10 10"><circle cx="4" cy="4" r="3" stroke="#fff" fill="none" stroke-width="1.2"/><path d="M6.3 6.3L9.5 9.5" stroke="#fff" stroke-width="1.2"/></svg>
  </div>
  <div class="listing" style="top:40px"><div class="ad"></div><div class="thumb" style="background:linear-gradient(#2a2622,#8a7a60)" role="img" aria-label="Photo of a restaurant entrance"></div><div class="n">Sora Terrace</div><div class="d">Ocean view dining with sunset deck<br>Kokusai St 525</div><div class="stars">★★★★<i>★</i></div><div class="price">$$$$</div><div class="km">3.8mi</div></div>
  <div class="listing" style="top:97px"><div class="ad"></div><div class="thumb" style="background:linear-gradient(#4a5660,#1e2428)" role="img" aria-label="Photo of a bar interior"></div><div class="n">Umi Bar and Dining</div><div class="d">Harbor Square, 264 Naminoue Rd, Naha 900-0031, Okinawa</div><div class="stars">★★★★<i>★</i></div><div class="price">$$$$</div><div class="km">4.9mi</div></div>
  <div class="listing" style="top:154px"><div class="thumb" style="background:linear-gradient(#5a8ab0,#c86a4a)" role="img" aria-label="Photo of a busy market restaurant"></div><div class="n">Kiyo Restaurant</div><div class="d">Cape Maeda Rd, Onna Village 904-0417, Okinawa</div><div class="stars">★★★★<i>★</i></div><div class="price">$$$</div><div class="km">5.0mi</div></div>
  <div class="listing" style="top:211px"><div class="thumb" style="background:linear-gradient(#3a3e44,#15171a)" role="img" aria-label="Photo of a dining room"></div><div class="n">Naha Grill House</div><div class="d">Makishi St, Naha 900-0013, Okinawa 1</div><div class="stars">★★★★<i>★</i></div><div class="price">$$$$</div><div class="km">5.2mi</div></div>
  <div class="listing" style="top:268px"><div class="thumb" style="background:linear-gradient(#8a5a30,#2a1a10)" role="img" aria-label="Photo of a warm lit restaurant"></div><div class="n">Ryukyu Catering House</div><div class="d">Green Hill Rd, Urasoe 901-2101, Okinawa 170</div><div class="stars">★★★★<i>★</i></div><div class="price">$$$</div><div class="km">5.2mi</div></div>
  <div class="listing" style="top:325px"><div class="thumb" style="background:linear-gradient(#e8e0d8,#8a6a5a)" role="img" aria-label="Photo of a dessert plate"></div><div class="n">Marco's Italian Naha</div><div class="d">Asato St, Naha 900-0001, Okinawa 140</div><div class="stars">★★★★<i>★</i></div><div class="price">$$$$</div><div class="km">5.6mi</div></div>
  <div class="listing" style="top:382px"><div class="n">Marco's Italian Naha</div></div>
</section>

</body>
</html>
```